How To Guide for Licensing Pet

3.5" x 2.5" playing card size. Two sided design, color is alright. Front side, City of Marlowton Pet License, and back side would be City of Kestrelton Dog License.
*Note both cities have different licensing requirements, dates and pricing.

Local License Fees
The City of Marlowton requires that all dogs and cats be licensed over the age of 6 months. Pet owners must purchase a license for their pet within thirty days of the date the pet is initially given the rabies vaccine and annually within thirty days’ time of the date of the current rabies vaccination. Licenses can be purchased at the Humane Society of Marlow Ridge with verification of a current rabies vaccination signed and administered by a licensed veterinarian.

Annual license fees are:

Neutered/spayed (altered) dog or cat – $10
Non-altered dog or cat – $30

To License: Current identification & current rabies vaccination certificate and bring to Humane Society of Marlow Ridge
4517 E Linden Grove Rd
Marlowton, IA 50999
563-555-0147

-
The City of Kestrelton requires every dog over 6 months of age be licensed. Licenses can be purchased at the Humane Society of Marlow Ridge . Pet licenses must be purchased prior to January 31 of each calendar year. Pet owners applying for a license must present a certificate of current rabies vaccination signed and administered by a licensed veterinarian.

Annual license fees are:

Neutered/spayed (altered) dog – $3
Non-altered dog – $25

4517 E Linden Grove Rd
Marlowton, IA 50999
563-555-0147

Target Market(s)

Animal Owners, easy to read

Industry/Entity Type

Pet

Requirements
Must have
• SIZE: 3.5" x 2.5" Playing Card Size
2 sides, Front: Marlowton, Back: Kestrelton.
Kestrelton only has Dog License requirement*

```html
<!DOCTYPE html>
<html lang="en">
<head>
<meta charset="utf-8">
<title>Pet License Guide – Marlowton &amp; Kestrelton</title>
<link href="https://fonts.googleapis.com/css2?family=Playfair+Display:wght@700&family=Arimo:ital,wght@0,400;0,700;1,400&display=swap" rel="stylesheet">
<style>
  :root {
    --ink: #111111;
    --page: #ffffff;
    --edge: #8a8a8a;
    --mar-head: #cfa28b;
    --mar-body: #ecddd3;
    --mar-mark: #b8775a;
    --kes-head: #7dc0c6;
    --kes-body: #d5e8ea;
    --kes-mark: #2a8a8f;
  }
  * { box-sizing: border-box; margin: 0; padding: 0; }
  html, body {
    width: 1200px; height: 797px; overflow: hidden;
    background: var(--page);
    font-family: "Arimo", Helvetica, Arial, sans-serif;
    color: var(--ink);
  }
  .sheet { position: relative; width: 1200px; height: 797px; }
  .card {
    position: absolute; top: 44px; width: 505px; height: 710px;
    border: 1px solid var(--edge);
    display: flex; flex-direction: column;
  }
  .card--marlowton { left: 49px; --head: var(--mar-head); --body: var(--mar-body); --mark: var(--mar-mark); }
  .card--kestrelton { left: 653px; --head: var(--kes-head); --body: var(--kes-body); --mark: var(--kes-mark); }

  .card__header {
    position: relative; height: 100px; background: var(--head);
    padding: 24px 0 0 45px;
    font-family: "Playfair Display", "Times New Roman", serif; font-weight: 700;
  }
  .card__kicker { font-size: 15px; letter-spacing: 1.5px; line-height: 1; }
  .card__city { font-size: 42px; letter-spacing: 5px; line-height: 1; margin-top: 0; }
  .card__mark { position: absolute; left: 421px; top: 26px; width: 56px; height: 54px; }

  .card__rules {
    height: 300px; background: var(--body);
    padding: 18px 60px 0 45px;
  }
  .section-title { font-weight: 700; font-size: 17.5px; line-height: 22px; }
  .rules-text { font-size: 17px; line-height: 21.3px; margin-top: 5px; }

  .card__fees {
    height: 106px; background: var(--page);
    padding: 19px 45px 0 45px;
  }
  .fee-list { list-style: none; margin-top: 5px; font-size: 17px; line-height: 19px; }
  .fee-list li { display: flex; }
  .fee-list .fee-label { width: 334px; }

  .card__contact {
    flex: 1; background: var(--body);
    padding: 19px 45px 0 45px;
  }
  .contact-lead { font-style: italic; font-size: 17px; line-height: 20px; }
  .contact-name { font-weight: 700; font-size: 17.5px; line-height: 22.5px; margin-top: 18px; }
  .contact-lines { font-size: 17.5px; line-height: 22.5px; font-style: normal; }
</style>
</head>
<body>
<main class="sheet">

  <article class="card card--marlowton">
    <header class="card__header">
      <p class="card__kicker">THE CITY OF</p>
      <h1 class="card__city">MARLOWTON</h1>
      <svg class="card__mark" viewBox="0 0 56 54" role="img" aria-label="Paw print icon">
        <rect x="0" y="0" width="56" height="54" rx="16" fill="var(--mark)"/>
      </svg>
    </header>
    <section class="card__rules">
      <h2 class="section-title">LOCAL LICENSE FEES</h2>
      <p class="rules-text">The City of Marlowton requires that all dogs and cats be licensed over the age of 6 months. Pet owners must purchase a license for their pet within thirty days of the date the pet is initially given the rabies vaccine and annually within thirty days’ time of the date of the current rabies vaccination. Licenses can be purchased at the Humane Society of Marlow Ridge with verification of a current rabies vaccination signed and administered by a licensed veterinarian.</p>
    </section>
    <section class="card__fees">
      <h2 class="section-title">ANNUAL LICENSE FEES (DOG OR CAT)</h2>
      <ul class="fee-list">
        <li><span class="fee-label">Neutered/spayed (altered)</span><span class="fee-price">$10</span></li>
        <li><span class="fee-label">Non-altered</span><span class="fee-price">$30</span></li>
      </ul>
    </section>
    <section class="card__contact">
      <p class="contact-lead">To Licence your pet bring current identification<br>&amp; current rabies vaccination certificate to:</p>
      <p class="contact-name">Humane Society of Marlow Ridge</p>
      <address class="contact-lines">4517 E Linden Grove Rd<br>Marlowton, IA 50999<br>563-555-0147</address>
    </section>
  </article>

  <article class="card card--kestrelton">
    <header class="card__header">
      <p class="card__kicker">THE CITY OF</p>
      <h1 class="card__city">KESTRELTON</h1>
      <svg class="card__mark" viewBox="0 0 56 54" role="img" aria-label="Paw print icon">
        <rect x="0" y="0" width="56" height="54" rx="16" fill="var(--mark)"/>
      </svg>
    </header>
    <section class="card__rules">
      <h2 class="section-title">LOCAL LICENSE FEES</h2>
      <p class="rules-text">The City of Kestrelton requires every dog over 6 months of age be licensed. Licenses can be purchased at the Humane Society of Marlow Ridge or from Kestrelton Civic Office. Pet licenses must be purchased prior to January 31 of each calendar year. Pet owners applying for a license must present a certificate of current rabies vaccination signed and administered by a licensed veterinarian.</p>
    </section>
    <section class="card__fees">
      <h2 class="section-title">ANNUAL LICENSE FEES (DOG)</h2>
      <ul class="fee-list">
        <li><span class="fee-label">Neutered/spayed (altered)</span><span class="fee-price">$3</span></li>
        <li><span class="fee-label">Non-altered</span><span class="fee-price">$25</span></li>
      </ul>
    </section>
    <section class="card__contact">
      <p class="contact-lead">To Licence your pet bring current identification<br>&amp; current rabies vaccination certificate to:</p>
      <p class="contact-name">Humane Society of Marlow Ridge</p>
      <address class="contact-lines">4517 E Linden Grove Rd<br>Marlowton, IA 50999<br>563-555-0147</address>
    </section>
  </article>

</main>
</body>
</html>
```